Coupons App Design Project

We have a simple coupons app with few screens and actions:
1. Very simple login screen (with chatterloop and findwell+)
2. Very simple business search page
3. Very simple business search results(each result contains logo icon, business name and delete icon)
4. business list (every row contains logo icon, business name and delete icon)
5. coupons list (each item contains image, title, subtitle, description, expiration time, status graphics (valid, expired, redeemed), delete icon
6. coupon view (image, title, subtitle, description, barcode etc.)
7. custom confirmation dialog(title, buttons, background, text)
8. "scan to subscribe" page (merchant name, merchant number, background image, text, barcode to scan etc.)
9. simple menu
10. splash screen

all graphics should be vector graphics so we can use it to different resolutions including for printing
Updates

Hi all, We've increased the project's budget by 25%. Thanks

Hi all,

We've decided to change the project from refundable to committed payment.
FYI

Hi All,

Thank you for your time and efforts, we really appreciate it.However we've eliminated most of the offered designs we've received becausethey didn't fit our desired look and feel.

Please download our look and feel file from our uploaded files -we've put there some examples of other apps that we like.

Thanks

Target Market(s)

shoppers all over the world

Industry/Entity Type

Business

Requirements
Must have
• Please take a look at the attached file "look & feel.jpg" for some nice screen shots taken from apps that we like

Should not have
• *****************************************************************************************
The attached files are only for demonstration purpose and needs descriptions so please don't send us design based on these screenshots.
*****************************************************************************************

```html
<!DOCTYPE html>
<html lang="en">
<head>
<meta charset="utf-8">
<title>Splash Screen</title>
<link rel="stylesheet" href="https://fonts.googleapis.com/css2?family=Lato:wght@400&family=Roboto:wght@400&display=swap">
<style>
  :root {
    --navy-deep: #072373;
    --navy: #0b3a99;
    --blue-glow: #1a7ad4;
    --blue-mid: #1462bf;
    --white: #ffffff;
    --status-bg: #000000;
    --status-icon: #e8e8e8;
    --status-dim: #7a7a7a;
    --battery-green: #7cc142;
  }
  html, body {
    margin: 0;
    padding: 0;
    width: 674px;
    height: 1200px;
    overflow: hidden;
    background: var(--navy-deep);
  }
  .screen {
    position: relative;
    width: 674px;
    height: 1200px;
    overflow: hidden;
    background:
      radial-gradient(ellipse 300px 300px at 650px 180px, var(--blue-glow) 0%, rgba(26,122,212,0) 100%),
      radial-gradient(ellipse 480px 620px at 337px 730px, var(--blue-glow) 0%, var(--blue-mid) 35%, var(--navy) 70%, var(--navy-deep) 100%);
  }
  .status-bar {
    position: absolute;
    top: 0; left: 0;
    width: 674px;
    height: 51px;
    background: var(--status-bg);
    font-family: 'Roboto', sans-serif;
    color: var(--status-icon);
  }
  .status-bar svg { position: absolute; top: 0; left: 0; }
  .status-battery-level {
    position: absolute;
    top: 10px;
    left: 412px;
    font-size: 27px;
    line-height: 32px;
  }
  .status-clock {
    position: absolute;
    top: 8px;
    left: 524px;
    font-size: 31px;
    line-height: 34px;
  }
  .splash-title {
    position: absolute;
    top: 389px;
    left: 0;
    width: 674px;
    height: 129px;
  }
  .title-rule {
    position: absolute;
    left: 84px;
    width: 548px;
    height: 3px;
    background: linear-gradient(90deg, rgba(255,255,255,0) 0%, rgba(255,255,255,0.55) 20%, var(--white) 50%, rgba(255,255,255,0.55) 80%, rgba(255,255,255,0) 100%);
  }
  .title-rule--top { top: 0; }
  .title-rule--bottom { bottom: 0; }
  .app-name {
    position: absolute;
    top: 0;
    left: 0;
    width: 674px;
    margin: 0;
    text-align: center;
    font-family: 'Lato', sans-serif;
    font-weight: 400;
    font-size: 88px;
    line-height: 129px;
    color: var(--white);
    letter-spacing: 0;
  }
</style>
</head>
<body>
  <main class="screen">
    <div class="status-bar">
      <svg width="674" height="51" viewBox="0 0 674 51" aria-hidden="true">
        <!-- usb connection icon -->
        <g fill="none" stroke="var(--status-dim)" stroke-width="3">
          <line x1="38" y1="10" x2="38" y2="42"/>
          <path d="M30 18 v8 l8 6"/>
          <path d="M46 16 v8 l-8 6"/>
        </g>
        <circle cx="38" cy="42" r="4" fill="var(--status-dim)"/>
        <!-- alarm icon -->
        <circle cx="330" cy="28" r="12" fill="none" stroke="var(--status-icon)" stroke-width="3.5"/>
        <path d="M330 20 v8 h6" fill="none" stroke="var(--status-icon)" stroke-width="3"/>
        <path d="M318 16 l-4 -4 M342 16 l4 -4" stroke="var(--status-icon)" stroke-width="4"/>
        <!-- signal icon -->
        <text x="363" y="18" font-family="Roboto, sans-serif" font-size="12" font-weight="700" fill="var(--status-icon)">H</text>
        <rect x="369" y="34" width="6" height="6" fill="var(--status-icon)"/>
        <rect x="377" y="27" width="6" height="13" fill="var(--status-icon)"/>
        <rect x="385" y="19" width="6" height="21" fill="var(--status-dim)"/>
        <rect x="393" y="11" width="6" height="29" fill="var(--status-dim)"/>
        <!-- battery icon -->
        <rect x="478" y="15" width="27" height="19" fill="none" stroke="var(--status-icon)" stroke-width="3"/>
        <rect x="505" y="20" width="3" height="9" fill="var(--status-icon)"/>
        <rect x="482" y="19" width="19" height="11" fill="var(--battery-green)"/>
        <path d="M494 18 l-6 8 h5 l-3 6 l8 -9 h-5 z" fill="var(--status-bg)"/>
      </svg>
      <span class="status-battery-level">54%</span>
      <span class="status-clock">12:08 pm</span>
    </div>

    <section class="splash-title">
      <div class="title-rule title-rule--top"></div>
      <h1 class="app-name">App name</h1>
      <div class="title-rule title-rule--bottom"></div>
    </section>
  </main>
</body>
</html>
```